Probation office requires Colourful A3 Poster to Celebrate our Success in previous year

We require a colourfull A3 Poster to promote our Success in the previous year within our Probation area. The Text we have in this poster (attached document) needs to stand out as much as possible on the poster so shadows and any other way of distinguishing text on the poster should be encouraged.
The theme of the poster is Success and celebration so any images in the poster should reflect this (example balloons, streamers, fireworks).
I have attached to this design the text which we require in the poster and also our company logo which we would require in the poster (ideally in the bottom right corner).
Many thanks for looking at this project
It Company

```html
<!DOCTYPE html>
<html lang="en">
<head>
<meta charset="utf-8">
<title>We're Exceptional – Northvale Probation Trust</title>
<link rel="stylesheet" href="https://fonts.googleapis.com/css2?family=Marcellus&family=Rye&display=swap">
<style>
  :root {
    --violet: #7a5aa6;
    --violet-deep: #6a4b98;
    --violet-soft: #9477bd;
    --pink: #c45a9c;
    --tile: #7b4f9e;
    --white: #ffffff;
    --cyan: #6fb6e6;
  }
  html, body {
    margin: 0;
    padding: 0;
    overflow: hidden;
    background: var(--violet);
  }
  .poster {
    position: relative;
    width: 848px;
    height: 1200px;
    overflow: hidden;
    background: var(--violet);
    color: var(--white);
    font-family: "Marcellus", serif;
  }
  .sky-scene {
    position: absolute;
    inset: 0;
    background:
      radial-gradient(ellipse 190px 240px at 300px 420px, rgba(196, 90, 156, 0.45), transparent 75%),
      radial-gradient(ellipse 70px 90px at 800px 520px, rgba(196, 90, 156, 0.35), transparent 75%),
      radial-gradient(ellipse 50px 65px at 665px 595px, rgba(210, 100, 160, 0.4), transparent 75%),
      radial-gradient(ellipse 45px 55px at 65px 290px, rgba(180, 90, 160, 0.35), transparent 75%),
      radial-gradient(ellipse 130px 260px at 820px 1010px, rgba(150, 90, 170, 0.5), transparent 75%),
      linear-gradient(180deg, var(--violet-deep) 0%, var(--violet) 45%, var(--violet-soft) 100%);
  }
  .balloon-cluster {
    position: absolute;
    left: 650px;
    top: 30px;
    width: 165px;
    height: 155px;
    border-radius: 50%;
    background: radial-gradient(circle at 45% 40%, var(--cyan) 0%, rgba(180, 110, 190, 0.85) 55%, transparent 72%);
  }
  .brand {
    position: absolute;
    left: 46px;
    top: 48px;
    width: 90px;
    height: 156px;
    background: var(--tile);
    outline: 1px solid rgba(255, 255, 255, 0.35);
  }
  .brand-mark {
    position: absolute;
    left: 22px;
    top: 14px;
    width: 46px;
    height: 46px;
    background: var(--white);
  }
  .brand-name {
    position: absolute;
    left: 0;
    right: 0;
    top: 100px;
    margin: 0;
    font-size: 11px;
    line-height: 13px;
    text-align: center;
    color: var(--white);
  }
  .title {
    position: absolute;
    left: 150px;
    width: 540px;
    top: 52px;
    margin: 0;
    font-family: "Rye", serif;
    font-weight: 400;
    font-size: 54px;
    line-height: 64px;
    text-align: center;
    letter-spacing: 2px;
    text-shadow: 2px 2px 4px rgba(0, 0, 0, 0.25);
  }
  .copy {
    position: absolute;
    margin: 0;
    font-size: 12px;
    line-height: 20px;
    text-align: center;
    text-transform: uppercase;
    text-shadow: 0 1px 3px rgba(0, 0, 0, 0.2);
  }
  .copy p { margin: 0; }
  .copy p + p { margin-top: 20px; }
  .achievements { left: 340px; width: 455px; top: 256px; }
  .headline {
    position: absolute;
    left: 0;
    width: 848px;
    top: 516px;
    margin: 0;
    font-family: "Rye", serif;
    font-weight: 400;
    font-size: 31px;
    line-height: 40px;
    text-align: center;
    letter-spacing: 1.5px;
    text-shadow: 2px 2px 4px rgba(0, 0, 0, 0.25);
  }
  .successes { left: 40px; width: 770px; top: 596px; }
  .impact { left: 40px; width: 770px; top: 792px; }
  .partnership { left: 40px; width: 770px; top: 972px; }
</style>
</head>
<body>
<main class="poster">
  <div class="sky-scene" role="img" aria-label="Photograph of hot air balloons rising across a purple evening sky"></div>
  <div class="balloon-cluster" role="img" aria-label="Photograph of a bunch of blue and pink party balloons"></div>

  <div class="brand">
    <span class="brand-mark"></span>
    <p class="brand-name">NORTHVALE<br>PROBATION<br>TRUST</p>
  </div>

  <h1 class="title">WE’RE<br>EXCEPTIONAL!</h1>

  <section class="copy achievements">
    <p>Brookfield Probation finished 2012-13 as an exceptionally performing district within Northvale Probation Trust</p>
    <p>Only district to:</p>
    <p>Deliver sustained performance for over two years<br>
       Achieve the highest % rating two consecutive years<br>
       Achieve exceptional in all five critical measures – offender accommodation, employment, quality of assessments and successful completion of orders/licences</p>
  </section>

  <h2 class="headline">WE REDUCED RE OFFENDING BY 9%</h2>

  <section class="copy successes">
    <p>Our successes include:</p>
    <p>80% of offenders are successfull in completing their orders and<br>
       licences. We supervised over 1,800 such sentences<br>
       When offenders on community orders failed to comply with the court order, we breached<br>
       97% of these offenders<br>
       When offenders failed to comply to protect the public we recalled 99% of these offenders</p>
  </section>

  <section class="copy impact">
    <p>It means:</p>
    <p>Our courts can have confidence in punishment in the community<br>
       Offenders are constructively managed with high quality interventions<br>
       Our communities can feel safer with the knowledge that we’re<br>
       reducing crime</p>
  </section>

  <section class="copy partnership">
    <p>We’re proud to be a key player in the local community safety<br>
       partnership where we make a visibly constructive contribution<br>
       It doesn’t end there…</p>
    <p>We continue to lead towards becoming a market leader in offender assessment and<br>
       offender management.<br>
       Our success means fewer victims and safer and stronger communities.</p>
  </section>
</main>
</body>
</html>
```